Add Responsiveness to Current Website

The website http://www.velvet-screen-room-studio.example needs to be made responsive. This includes all the menus and all the galleries. The Design, graphics, colors can remain the same, except I can provide larger images and design for the Home Page. If you know what you are doing, this should not take too long.

Coding

Coded - Design and coding required

Number of Pages Required

5+ page

Font styles to use
Sans Serif

Colors
f37122
f78f20

Requirements
Must have
• Responsive Menus and Galleries

```html
<!DOCTYPE html>
<html lang="en">
<head>
<meta charset="utf-8">
<title>Velvet Screen – Home Theater Design</title>
<link href="https://fonts.googleapis.com/css2?family=Open+Sans:ital,wght@0,400;0,600;0,700;1,400&family=Montserrat:wght@400;500;600&family=Roboto+Condensed:wght@300&family=Lora&display=swap" rel="stylesheet">
<style>
:root{
  --orange:#f37122;
  --orange-light:#f78f20;
  --navy:#1d2a45;
  --navy-deep:#18233b;
  --stage:#5b5a57;
  --ink:#222;
  --muted:#9a9a9a;
  --line:#d8d8d8;
  --white:#fff;
}
*{margin:0;padding:0;box-sizing:border-box}
html,body{width:960px;height:1200px;overflow:hidden;background:var(--stage)}
body{font-family:"Open Sans",sans-serif;color:var(--ink)}
.page{position:absolute;left:188.8px;top:0;width:700px;height:1500px;transform:scale(.8);transform-origin:0 0;background:var(--white);overflow:hidden}
.abs{position:absolute}

/* top bar */
.topbar{left:0;top:0;width:700px;height:22px;background:var(--orange-light);font-size:5.5px;color:#3a2a10;font-weight:600}
.topbar span{position:absolute;top:7px;display:flex;align-items:center;gap:3px}
.topbar svg{width:6px;height:6px}
.social-top{position:absolute;right:82px;top:8px;display:flex;gap:7px}
.social-top i{display:block;width:5px;height:5px;border-radius:50%;border:1px solid rgba(255,255,255,.75)}

/* header */
.header{left:0;top:22px;width:700px;height:60px;border-bottom:1px solid #eee}
.brand{position:absolute;left:38px;top:17px;display:flex;align-items:center;gap:6px;font-weight:700;font-size:23px;color:#8c7a1e}
.brand i{width:15px;height:15px;background:#8c7a1e;border-radius:50%}
.nav{position:absolute;left:243px;top:25px;display:flex;font-family:"Montserrat",sans-serif;font-size:7.5px;font-weight:500}
.nav a{color:#222;text-decoration:none;margin-right:18px}
.nav a.active{color:var(--orange-light)}
.nav .bracket{color:var(--orange-light);margin-right:8px}
.search{position:absolute;left:610px;top:25px;width:9px;height:9px}

/* hero */
.hero{left:0;top:82px;width:700px;height:281px;background:linear-gradient(172deg,#f3c57e 0%,#b48c5c 6%,#8e7352 22%,#7d6447 45%,#5e4630 68%,#3a2a1b 85%,#1f150d 100%)}
.hero-title{position:absolute;left:340px;top:195px;font-family:"Roboto Condensed",sans-serif;font-weight:300;font-size:31px;letter-spacing:-1.5px;color:#fff}
.hero-title em{font-style:normal;color:var(--orange-light)}
.hero-sub{position:absolute;left:341px;top:231px;font-family:"Lora",serif;font-size:15px;color:#f3eee5}
.hero-mark{position:absolute;left:324px;top:211px;width:4px;height:9px;background:#fff}

/* call band */
.callout{left:0;top:363px;width:700px;height:68px;background:var(--orange)}
.callout p{position:absolute;left:44px;top:27px;font-size:9px;font-weight:400;color:#fff}
.btn-quote{position:absolute;left:552px;top:22px;width:68px;height:23px;background:#fff;font-family:"Montserrat",sans-serif;font-size:6px;font-weight:600;display:flex;align-items:center;justify-content:center;color:#222}

/* features */
.feature{position:absolute;top:447px}
.feature .thumb{height:96px}
.feature h3{font-size:7.5px;font-weight:400;margin:13px 0 0 3px}
.feature p{font-size:5.6px;line-height:10.5px;color:var(--muted);margin:8px 0 0 3px;width:170px}
.btn{display:inline-flex;align-items:center;justify-content:center;width:57px;height:20px;font-family:"Montserrat",sans-serif;font-size:5.5px;font-weight:600;margin:12px 0 0 3px}
.btn-solid{background:var(--orange-light);color:#fff}
.btn-ghost{border:1px solid #ccc;color:#aaa;background:#fff}

/* projects */
.projects{left:0;top:662px;width:700px;height:256px;background:var(--navy)}
.projects h2{position:absolute;left:0;width:646px;top:32px;text-align:center;font-weight:400;font-size:10px;color:#fff}
.projects .rule{position:absolute;left:233px;top:55px;width:183px;height:1px;background:#3a4866}
.filters{position:absolute;left:179px;top:76px;font-size:7px;color:#dfe3ea;display:flex;gap:8px}
.filters .on{color:var(--orange-light)}
.gallery{position:absolute;left:57px;top:110px;display:flex}
.gallery div{width:134px;height:115px}
.arrow{position:absolute;top:158px;width:20px;height:20px;background:var(--orange-light);display:flex;align-items:center;justify-content:center}
.view{position:absolute;left:228px;top:166px;width:58px;height:17px;border:1px solid #fff;color:#fff;font-size:5px;font-family:"Montserrat",sans-serif;display:flex;align-items:center;justify-content:center;background:rgba(0,0,0,.45)}

/* about */
.section-title{position:absolute;left:0;width:704px;text-align:center;font-weight:700;font-size:12px}
.under{position:absolute;height:2px;width:50px;background:var(--orange-light)}
.who-text{position:absolute;left:236px;top:978px;width:200px}
.who-text h3{font-size:8.5px;font-weight:400}
.who-text p{font-size:5.5px;line-height:10.5px;color:#777;margin-top:9px}
.caption{position:absolute;left:451px;top:1082px;width:172px;font-family:"Lora",serif;font-size:5px;line-height:10.7px;color:#9a9a9a}

/* testimonials */
.testimonials{left:0;top:1132px;width:700px;height:188px;background:linear-gradient(180deg,#2a3550 0%,#3a4560 40%,#46506a 60%,#2d374d 100%)}
.testimonials h2{position:absolute;left:0;width:703px;top:32px;text-align:center;font-size:11px;font-weight:600;color:#fff;letter-spacing:.5px}
.quote{position:absolute;left:110px;width:484px;top:76px;text-align:center;font-size:7px;line-height:12px;color:#fff}
.who-name{position:absolute;left:0;width:703px;top:111px;text-align:center;color:var(--orange-light);font-weight:600;font-size:8px}
.who-role{position:absolute;left:0;width:703px;top:123px;text-align:center;color:#fff;font-style:italic;font-size:5.5px}
.qmark{position:absolute;top:78px;font-family:"Montserrat",sans-serif;font-size:36px;font-weight:600;color:#c9cdd4;line-height:1}
.dots{position:absolute;left:341px;top:145px;display:flex;gap:3px}
.dots i{width:5px;height:5px;border-radius:50%;border:1px solid #fff}
.dots i.on{background:var(--orange-light);border-color:var(--orange-light)}

/* footer */
.gap{left:0;top:1320px;width:700px;height:8px;background:var(--stage)}
.footer{left:0;top:1328px;width:700px;height:172px;background:var(--navy-deep)}
.col{position:absolute;top:36px;width:194px}
.col h4{font-family:"Montserrat",sans-serif;font-weight:500;font-size:10px;color:#fff}
.col .bar{margin-top:12px;height:1px;background:#39445c;position:relative}
.col .bar::before{content:"";position:absolute;left:0;top:-1px;width:42px;height:2px;background:var(--orange)}
.foot-brand{margin-top:20px;font-family:"Roboto Condensed",sans-serif;font-weight:300;font-size:17px;letter-spacing:-.8px;color:#fff}
.foot-text{margin-top:10px;font-size:6px;line-height:12.5px;color:#6f7a8f}
.links{display:grid;grid-template-columns:106px 100px;row-gap:9px;margin-top:17px;font-size:5.5px;color:#cfd4dd}
.links span::before{content:"›";color:#7c869a;margin-right:6px}
.links .on{color:var(--orange-light)}
.contact{margin-top:17px;display:flex;flex-direction:column;gap:8.7px;font-size:5.5px;color:#9aa3b3}
.contact div{display:flex;align-items:center;gap:15px}
.contact svg{width:8px;height:8px}
.foot-social{display:flex;gap:8px;margin-top:12px}
.foot-social i{width:6px;height:6px;border-radius:50%;background:#8b93a4}
.foot-social i:first-child{background:var(--orange)}
</style>
</head>
<body>
<div class="page">

  <div class="abs topbar">
    <span style="left:84px"><svg viewBox="0 0 10 10"><path d="M2 1l2 2-1 1.5a6 6 0 003 3L7.5 6l2 2-1.5 1.5C4 9 1 6 .5 2.5z" fill="#3a2a10"/></svg>555-014-2290</span>
    <span style="left:146px"><svg viewBox="0 0 10 10"><circle cx="5" cy="5" r="4" fill="none" stroke="#3a2a10"/><path d="M5 2.5V5h2" stroke="#3a2a10" fill="none"/></svg>Mon - Sat: 9:00 - 18:00</span>
    <span style="left:238px"><svg viewBox="0 0 10 10"><rect x="1" y="2" width="8" height="6" fill="none" stroke="#3a2a10"/><path d="M1 2l4 3 4-3" fill="none" stroke="#3a2a10"/></svg>hello@velvetscreen.example</span>
    <div class="social-top"><i></i><i></i><i></i><i></i><i></i><i></i></div>
  </div>

  <header class="abs header">
    <div class="brand"><i></i>Velvet Screen</div>
    <nav class="nav">
      <span class="bracket">[</span>
      <a class="active" href="#">HOME</a>
      <a href="#">ABOUT</a>
      <a href="#">PRODUCTS</a>
      <a href="#">OUR GALLERY</a>
      <a href="#">OUR STORY</a>
      <a href="#">CONTACT</a>
    </nav>
    <svg class="search" viewBox="0 0 10 10"><circle cx="4" cy="4" r="3" fill="none" stroke="#222" stroke-width="1.4"/><path d="M6.3 6.3L9 9" stroke="#222" stroke-width="1.4"/></svg>
  </header>

  <section class="abs hero" role="img" aria-label="Photo of a warmly lit home theater room with a wall screen, framed movie posters and dark leather seating">
    <div class="hero-mark"></div>
    <div class="hero-title">Home Theater <em>Design</em></div>
    <div class="hero-sub">Most Versatile Room In Your Home</div>
  </section>

  <section class="abs callout">
    <p>Call Today (555-014-2290) To Discuss All Your Home Theater Design Options</p>
    <div class="btn-quote">GET A QUOTE</div>
  </section>

  <article class="feature" style="left:82px">
    <div class="thumb" style="width:177px;background:linear-gradient(180deg,#6e5236 0%,#8a6a46 30%,#5a4230 60%,#2a1d14 100%)" role="img" aria-label="Theater room lined with artisan acoustic panels"></div>
    <h3>Artesian Panels</h3>
    <p>Nam viverra scelerisque turpis id fermentum. Sed bibendum sit amet odio tempor venenatis. Quisque vel lectus sem. Sed convallis ligula sit amet.</p>
    <span class="btn btn-solid">READ MORE</span>
  </article>
  <article class="feature" style="left:267px">
    <div class="thumb" style="width:164px;background:linear-gradient(100deg,#3a2a5a 0%,#8a5a8a 25%,#c08a60 50%,#5a4a6a 75%,#2a2638 100%)" role="img" aria-label="Space-themed theater room with planet murals"></div>
    <h3>Universal Theme</h3>
    <p>Nam viverra scelerisque turpis id fermentum. Sed bibendum sit amet odio tempor venenatis. Quisque vel lectus sem. Sed convallis ligula sit amet.</p>
    <span class="btn btn-ghost">READ MORE</span>
  </article>
  <article class="feature" style="left:442px">
    <div class="thumb" style="width:170px;background:linear-gradient(90deg,#2a1e16 0%,#4a3626 28%,#8a7c68 50%,#a39886 75%,#988c7a 100%)" role="img" aria-label="Fabric-covered wall with a wall sconce"></div>
    <h3>Conventional Fabrics</h3>
    <p>Nam viverra scelerisque turpis id fermentum. Sed bibendum sit amet odio tempor venenatis. Quisque vel lectus sem. Sed convallis ligula sit amet.</p>
    <span class="btn btn-ghost">READ MORE</span>
  </article>

  <section class="abs projects">
    <h2>Completed Projects</h2>
    <div class="rule"></div>
    <div class="filters"><span class="on">[ ALL PROJECTS ]</span><span>Home Theater Rooms</span><span>|</span><span>Other Porjects</span></div>
    <div class="gallery">
      <div style="background:linear-gradient(90deg,#6a1e26 0%,#b0605a 30%,#7a2a2e 60%,#c0403a 85%,#5a1a1c 100%)" role="img" aria-label="Theater with red decorative wall panels"></div>
      <div style="background:linear-gradient(180deg,#e0ddd6 0%,#b6b2aa 40%,#5a5852 70%,#1e1d1a 100%)" role="img" aria-label="Bright theater room with projector and seating"></div>
      <div style="background:linear-gradient(180deg,#1a1a22 0%,#4a3e36 45%,#7a3a2a 75%,#a02a22 100%)" role="img" aria-label="Space mural theater with red seats"></div>
      <div style="background:linear-gradient(110deg,#2a4a80 0%,#5a8ac0 35%,#c0c8d8 55%,#d05a3a 75%,#1a2a4a 100%)" role="img" aria-label="Theater screen showing a car"></div>
    </div>
    <div class="view">VIEW PROJECT</div>
    <div class="arrow" style="left:46px"><svg width="8" height="8" viewBox="0 0 10 10"><path d="M6.5 2L3.5 5l3 3" fill="none" stroke="#fff" stroke-width="1.6"/></svg></div>
    <div class="arrow" style="left:581px"><svg width="8" height="8" viewBox="0 0 10 10"><path d="M3.5 2l3 3-3 3" fill="none" stroke="#fff" stroke-width="1.6"/></svg></div>
  </section>

  <h2 class="section-title" style="top:930px">WHO WE ARE?</h2>
  <div class="under" style="left:327px;top:954px"></div>
  <div class="abs" style="left:84px;top:983px;width:138px;height:120px;background:radial-gradient(ellipse at 50% 60%,#4aa0c0 0%,#2a5a70 12%,#7a3420 30%,#a0582c 50%,#4a1e12 80%,#2a1008 100%)" role="img" aria-label="Ornate theater room with a large screen"></div>
  <div class="who-text">
    <h3>Home Theater Design</h3>
    <p>In terms of design, your Home Theater is the most versatile room in your home. Your options are limitless. You can compliment your existing home decor or you can create a design that is completely different from the rest of your home.</p>
    <p>If you enjoy exploring unique design opportunities, our decorative acoustic panels can act as a canvas for your inspiration.</p>
  </div>
  <span class="btn btn-ghost abs" style="left:235px;top:1085px;margin:0">READ MORE</span>
  <div class="abs" style="left:446px;top:968px;width:180px;height:104px;background:linear-gradient(180deg,#a0502e 0%,#c47a52 35%,#6a4a3a 65%,#3a2a22 100%)" role="img" aria-label="Theater room with canyon landscape panels and leather seats"></div>
  <p class="caption">The moment you contact Velvet Screen, you will talk directly with Dale Renner, the President and founder of the company. You will continue this personal dialog with Dale throughout the entire</p>

  <section class="abs testimonials" role="img" aria-label="Dimmed photo of a theater room behind the testimonials">
    <h2>TESTIMONIALS</h2>
    <div class="under" style="left:327px;top:54px"></div>
    <div class="qmark" style="left:84px">“</div>
    <p class="quote">I've been happy with the services provided by Northfield Builders. Marcy Dunn has been wonderful! She has returned my calls quickly, and she answered all my questions. This is required when, for example, the final text is not yet available.</p>
    <div class="qmark" style="left:600px">”</div>
    <div class="who-name">Tessa Morrow</div>
    <div class="who-role">Founder &amp; CEO Brightlane Media Ltd..</div>
    <div class="dots"><i class="on"></i><i></i><i></i></div>
  </section>

  <div class="abs gap"></div>

  <footer class="abs footer">
    <div class="col" style="left:56px">
      <h4>About Us</h4>
      <div class="bar" style="width:42px"></div>
      <div class="foot-brand">Your Home Theater</div>
      <p class="foot-text">Sed ut perspiciatis unde omnis iste natus error sit voluptat accusantium doloremque laudantium, totam rem aperiam.</p>
      <div class="foot-social"><i></i><i></i><i></i><i></i><i></i><i></i></div>
    </div>
    <div class="col" style="left:267px">
      <h4>Infomation</h4>
      <div class="bar"></div>
      <div class="links">
        <span>About Us</span><span>Who We Are</span>
        <span class="on">Overview</span><span>Our Services</span>
        <span>Our Team</span><span>Projects</span>
        <span>Innovation</span><span>Careers</span>
        <span>Testimonials</span><span>Contact Us</span>
      </div>
    </div>
    <div class="col" style="left:478px;width:194px">
      <h4>Structure Office</h4>
      <div class="bar"></div>
      <div class="contact">
        <div><svg viewBox="0 0 10 10"><path d="M5 9.5S1.8 6 1.8 4a3.2 3.2 0 016.4 0C8.2 6 5 9.5 5 9.5z" fill="#8b93a4"/></svg>22 Harbor Lane, Westbrook</div>
        <div><svg viewBox="0 0 10 10"><path d="M2 1l2 2-1 1.5a6 6 0 003 3L7.5 6l2 2-1.5 1.5C4 9 1 6 .5 2.5z" fill="#8b93a4"/></svg>(555) 0140 2291</div>
        <div><svg viewBox="0 0 10 10"><rect x="1" y="2" width="8" height="6" fill="#8b93a4"/><path d="M1 2l4 3 4-3" fill="none" stroke="#18233b"/></svg>office@velvetscreen.example</div>
        <div><svg viewBox="0 0 10 10"><rect x="1" y="2" width="8" height="7" fill="#8b93a4"/><rect x="3" y="1" width="4" height="2" fill="#8b93a4"/></svg>(555) 0140 2292</div>
        <div><svg viewBox="0 0 10 10"><circle cx="5" cy="5" r="4" fill="none" stroke="#8b93a4"/><path d="M5 2.5V5h2" stroke="#8b93a4" fill="none"/></svg>Mon - Sat: 9:00 - 18:00</div>
      </div>
    </div>
  </footer>

</div>
</body>
</html>
```